Packaging for Hair Fibers Product

We are a start up company looking for a new packaging design for hair building fibers. These are aimed at predominantly men but also women as well. We already have a logo and i have the packaging design from our competitors. We are wanting to keep the look masculine as 90% of our users will be middle aged men. We would like the colours to be black and white but are open to other colours as well.
It will need to have our logo and the following somewhere on the front.
"Instant Fuller & Thicker Hair" & "Natural Hair Building Fibers" "28g" or "Net Weight 28g"
We only need the front of the packaging designed, please make the other sides of the packaging the same colour but blank.
Target Market(s)
Men 25+
Industry/Entity Type
Hair And Beauty
Requirements
Must have
- Logo which i have included. and the following somewhere on the front.
- "Instant Fuller & Thicker Hair" ; "Natural Hair Building Fibers" "28g" or "Net Weight 28g"
Nice to have
- Make it stand out from the competition or similar to the palirox example.

```html
<!DOCTYPE html>
<html lang="en">
<head>
<meta charset="utf-8">
<title>Densora Hair Building Fibers – Front Panel</title>
<link rel="stylesheet" href="https://fonts.googleapis.com/css2?family=Dosis:wght@300&display=swap">
<style>
  :root {
    --backdrop: #e4e4e4;
    --panel: #050505;
    --ink: #f4f4f4;
    --accent-light: #f0821e;
    --accent-mid: #c5451a;
    --accent-dark: #5a1a10;
  }
  html, body {
    margin: 0;
    padding: 0;
    width: 1200px;
    height: 884px;
    overflow: hidden;
    background: var(--backdrop);
  }
  .canvas {
    position: relative;
    width: 1200px;
    height: 884px;
  }
  .front-panel {
    position: absolute;
    left: 402px;
    top: 42px;
    width: 396px;
    height: 800px;
    background: var(--panel);
    color: var(--ink);
    font-family: "Dosis", sans-serif;
    font-weight: 300;
    overflow: hidden;
  }
  .accent {
    position: absolute;
    display: block;
  }
  .accent-top { right: 0; top: 0; width: 116px; height: 248px; }
  .accent-bottom { left: 0; bottom: 0; width: 108px; height: 208px; }
  .brand-name {
    position: absolute;
    left: 0;
    right: 0;
    top: 176px;
    text-align: center;
    font-size: 44px;
    letter-spacing: 6px;
    margin: 0;
  }
  .brand-mark {
    display: inline-block;
    width: 12px;
    height: 12px;
    background: var(--ink);
    margin-left: 4px;
    vertical-align: middle;
  }
  .product-name {
    position: absolute;
    left: 0;
    right: 0;
    top: 336px;
    margin: 0;
    text-align: center;
    font-size: 38px;
    line-height: 1.35;
    font-weight: 300;
  }
  .tagline {
    position: absolute;
    left: 0;
    right: 0;
    top: 610px;
    margin: 0;
    text-align: center;
    font-size: 23px;
  }
  .net-weight {
    position: absolute;
    left: 0;
    right: 0;
    top: 730px;
    margin: 0;
    text-align: center;
    font-size: 17px;
  }
</style>
</head>
<body>
<main class="canvas">
  <section class="front-panel">
    <svg class="accent accent-top" viewBox="0 0 116 248" role="img" aria-label="Faceted orange triangle pattern">
      <defs>
        <linearGradient id="accentTopFill" x1="0" y1="0" x2="0.4" y2="1">
          <stop offset="0" stop-color="var(--accent-dark)"/>
          <stop offset="0.55" stop-color="var(--accent-mid)"/>
          <stop offset="1" stop-color="var(--accent-light)"/>
        </linearGradient>
      </defs>
      <polygon points="0,0 116,0 116,248" fill="url(#accentTopFill)"/>
    </svg>

    <p class="brand-name">DENSORA<span class="brand-mark"></span></p>

    <h1 class="product-name">Natural Hair<br>Building Fibers</h1>

    <p class="tagline">Instant Fuller &amp; Thicker Hair</p>

    <p class="net-weight">Net Weight 28g</p>

    <svg class="accent accent-bottom" viewBox="0 0 108 208" role="img" aria-label="Faceted orange triangle pattern">
      <defs>
        <linearGradient id="accentBottomFill" x1="0" y1="0" x2="0.5" y2="1">
          <stop offset="0" stop-color="var(--accent-light)"/>
          <stop offset="0.5" stop-color="var(--accent-mid)"/>
          <stop offset="1" stop-color="var(--accent-dark)"/>
        </linearGradient>
      </defs>
      <polygon points="0,0 108,208 0,208" fill="url(#accentBottomFill)"/>
    </svg>
  </section>
</main>
</body>
</html>
```